Dog care service needs advertising poster

Our company is Paw Haven. We provide care for dogs while their owners are away, either through home visits or a holiday stay in the homes of carefully selected minders. Our existing website & Facebook cover should provide all the colour cues for a poster - namely blues, blondes and grey. We have an existing logo (provided). We can feature the same imagery from our website as I have purchased the rights to the stock images.

www.pawhavenexample.com.au
www.facebook.com/pawhavenexampleau

This brief is for design of a poster that can be placed in vet surgeries, groomers, on community noticeboards. It should be scalable to print in three sizes, A5, A4 & A3.

We wish to clearly communicate our three areas of service "dog minding, home visits, dog walking".

We would like to have the files ready for upload to Printora (or similar) for immediate printing.

Target Market(s)

Dog owners who love their dogs like family.

Industry/Entity Type

Advertising

Font styles to use
Sans Serif

Colors
33a6d7
3276b5

Requirements
Must have
• Logo
• www.pawhavenexample.com.au
• Telephone number
• Three services - Dog Minding, Home Visits, Dog Walking
Nice to have
• use of our existing stock photography to highlight the three areas of service - Dog minding, home visits, dog walking. Existing colour palette - blues, blondes and grey.
• Text that can be used:
• Western Sydney’s complete dog care service.
• Dog Minding - Your dog stays in the home of one of our carefully selected minders.Treated like part of the family, they enjoy all the creature comforts they are used to.
• Home Visits - We visit your dog at your home for feeding, walking and playtime. Short of long visits available.
• Dog Walking - If you can't walk your dog for any reason we are here to help. 1/2 hour or hourly walks available.
• Contact us today for a tailored package to meet your needs.
Should not have
• Any additional illustrations beyond the logo.

```html
<!DOCTYPE html>
<html lang="en">
<head>
<meta charset="utf-8">
<title>Paw Haven – Dog Care Poster</title>
<link href="https://fonts.googleapis.com/css2?family=Oswald:wght@500;600&family=Great+Vibes&family=Arimo:ital,wght@0,400;0,700;1,400&display=swap" rel="stylesheet">
<style>
  :root {
    --page-bg: #5b5b5b;
    --sky: #33a6d7;
    --ocean: #3276b5;
    --deep: #1d5a9a;
    --band: #5cbbe6;
    --ink: #2f3d4f;
    --white: #ffffff;
    --teal: #3f9a9c;
    --blonde: #d9ab6a;
    --oval-ring: #6cc4ec;
  }
  * { box-sizing: border-box; margin: 0; padding: 0; }
  html, body { width: 1169px; height: 1200px; overflow: hidden; background: var(--page-bg); }
  .poster {
    position: absolute; left: 184px; top: 34px;
    width: 800px; height: 1131px; overflow: hidden;
    background: var(--ocean);
    box-shadow: 0 12px 40px rgba(0,0,0,.45);
    font-family: "Arimo", Arial, sans-serif;
    color: var(--white);
  }
  .poster-art { position: absolute; inset: 0; }
  .brand { position: absolute; left: 30px; top: 60px; display: flex; align-items: center; gap: 16px; }
  .brand-mark { width: 70px; height: 70px; border-radius: 50%; background: var(--ink); }
  .brand-name { font-weight: 700; font-size: 50px; color: var(--ink); letter-spacing: -.5px; }
  .tagline {
    position: absolute; right: 50px; top: 186px; text-align: right;
    font-family: "Great Vibes", cursive; font-size: 50px; line-height: 53px; color: var(--white);
    text-shadow: 0 1px 3px rgba(0,40,90,.35);
  }
  .contact { position: absolute; left: 18px; top: 500px; width: 340px; text-align: center; white-space: nowrap; }
  .contact-phone { display: flex; align-items: center; justify-content: center; gap: 10px;
    font-family: "Oswald", sans-serif; font-weight: 600; font-size: 40px; line-height: 1;
    text-shadow: 0 2px 0 var(--deep), 0 0 6px rgba(0,30,80,.5); }
  .phone-icon { width: 44px; height: 44px; border-radius: 8px; background: var(--white); display: grid; place-items: center; }
  .contact-cta { font-family: "Oswald", sans-serif; font-weight: 600; font-size: 40px; line-height: 1.15; margin-top: 6px;
    text-shadow: 0 2px 0 var(--deep), 0 0 6px rgba(0,30,80,.5); }
  .contact-note { font-style: italic; font-size: 23px; line-height: 25px; margin-top: 2px; text-shadow: 0 1px 3px rgba(0,20,60,.8); }
  .service { position: absolute; top: 928px; }
  .service-title { font-family: "Oswald", sans-serif; font-weight: 600; font-size: 33px; line-height: 1; text-align: center;
    text-shadow: 0 2px 0 #0d2a4a, 0 0 4px rgba(0,0,0,.6); white-space: nowrap; letter-spacing: -.3px; }
  .service-text { font-size: 15px; line-height: 18.5px; margin-top: 10px; }
  .service--minding { left: 48px; width: 220px; }
  .service--visits { left: 302px; width: 212px; }
  .service--walking { left: 538px; width: 240px; }
  .footer-rule { position: absolute; left: 30px; right: 30px; top: 1078px; border-top: 2px dotted var(--band); }
  .footer { position: absolute; top: 1086px; left: 46px; right: 40px; height: 40px; display: flex; align-items: center;
    font-family: "Oswald", sans-serif; font-weight: 500; font-size: 28px; }
  .footer-item { display: flex; align-items: center; gap: 10px; }
  .footer-item--web { margin-left: 70px; }
</style>
</head>
<body>
<main class="poster">
  <svg class="poster-art" width="800" height="1131" viewBox="0 0 800 1131">
    <defs>
      <linearGradient id="paperGrad" x1="0" y1="0" x2="1" y2="1">
        <stop offset="0" stop-color="#ffffff"/><stop offset="1" stop-color="#dfe8ef"/>
      </linearGradient>
      <linearGradient id="blueGrad" x1="0" y1="0" x2="1" y2="1">
        <stop offset="0" stop-color="#4aa9dc"/><stop offset="1" stop-color="#2f7cbf"/>
      </linearGradient>
      <linearGradient id="seaGrad" x1="0" y1="0" x2="0" y2="1">
        <stop offset="0" stop-color="#9fcbe6"/><stop offset=".5" stop-color="#3e8fc4"/><stop offset="1" stop-color="#2a6fae"/>
      </linearGradient>
      <linearGradient id="dogGrad" x1="0" y1="0" x2="0" y2="1">
        <stop offset="0" stop-color="#3f9a9c"/><stop offset=".6" stop-color="#3a8fa0"/><stop offset=".72" stop-color="#c9a56e"/><stop offset="1" stop-color="#d9ab6a"/>
      </linearGradient>
      <linearGradient id="dogFade" x1="0" y1="0" x2="1" y2="0">
        <stop offset="0" stop-color="#fff" stop-opacity="0"/><stop offset=".3" stop-color="#fff" stop-opacity="1"/>
      </linearGradient>
      <mask id="dogMask"><rect x="300" y="280" width="455" height="660" fill="url(#dogFade)"/></mask>
      <linearGradient id="oval1" x1="0" y1="0" x2="0" y2="1"><stop offset="0" stop-color="#8fc3e6"/><stop offset="1" stop-color="#6f9a3a"/></linearGradient>
      <linearGradient id="oval2" x1="0" y1="0" x2="0" y2="1"><stop offset="0" stop-color="#d8cdbd"/><stop offset="1" stop-color="#9a6a40"/></linearGradient>
      <linearGradient id="oval3" x1="0" y1="0" x2="0" y2="1"><stop offset="0" stop-color="#dfe6e0"/><stop offset="1" stop-color="#5f8f3a"/></linearGradient>
    </defs>
    <rect width="800" height="1131" fill="url(#blueGrad)"/>
    <rect x="0" y="470" width="420" height="480" fill="url(#seaGrad)" role="img" aria-label="Photo of the sea and horizon"/>
    <path d="M0,0 H565 C480,90 330,130 270,240 C220,330 130,400 0,450 Z" fill="url(#paperGrad)"/>
    <rect x="300" y="280" width="455" height="660" fill="url(#dogGrad)" mask="url(#dogMask)" role="img" aria-label="Photo of a golden retriever sitting, seen from the side"/>
    <rect x="755" y="0" width="30" height="1131" fill="var(--band)" opacity=".75"/>
    <path d="M0,870 C150,845 320,990 520,960 C640,942 720,900 800,880 V1131 H0 Z" fill="var(--deep)"/>
    <path d="M0,880 C160,860 320,1000 520,972 C640,955 720,915 800,895" fill="none" stroke="var(--band)" stroke-width="4" opacity=".8"/>
    <path d="M0,900 C170,880 330,1012 530,985 C650,968 730,930 800,912" fill="none" stroke="#7cc9ee" stroke-width="2" opacity=".6"/>
    <g stroke="var(--oval-ring)" stroke-width="5">
      <ellipse cx="180" cy="790" rx="92" ry="115" fill="url(#oval1)" role="img" aria-label="Photo of a dog sitting on grass"/>
      <ellipse cx="402" cy="790" rx="88" ry="115" fill="url(#oval2)" role="img" aria-label="Photo of a dog on a home doormat"/>
      <ellipse cx="622" cy="790" rx="88" ry="115" fill="url(#oval3)" role="img" aria-label="Photo of a bulldog on a lead in a park"/>
    </g>
  </svg>

  <div class="brand">
    <span class="brand-mark"></span>
    <span class="brand-name">Paw Haven</span>
  </div>

  <p class="tagline">Western Sydney’s<br>complete dog<br>care service</p>

  <div class="contact">
    <div class="contact-phone">
      <span class="phone-icon">
        <svg width="26" height="26" viewBox="0 0 24 24"><path fill="#3276b5" d="M6.6 10.8a15 15 0 0 0 6.6 6.6l2.2-2.2a1 1 0 0 1 1-.25 11.4 11.4 0 0 0 3.6.57 1 1 0 0 1 1 1V20a1 1 0 0 1-1 1A17 17 0 0 1 3 4a1 1 0 0 1 1-1h3.5a1 1 0 0 1 1 1c0 1.25.2 2.45.57 3.57a1 1 0 0 1-.25 1z"/></svg>
      </span>
      0400 555 019
    </div>
    <div class="contact-cta">CONTACT US TODAY</div>
    <p class="contact-note">for a tailored package<br>to meet your needs.</p>
  </div>

  <section class="service service--minding">
    <h2 class="service-title">DOG MINDING</h2>
    <p class="service-text">Your dog stays in the home of one of our carefully selected minders. Treated like part of the family, they enjoy all the creature comforts they are used to.</p>
  </section>
  <section class="service service--visits">
    <h2 class="service-title">HOME VISITS</h2>
    <p class="service-text">We visit your dog at your home for feeding, walking and playtime. Short of long visits available.</p>
  </section>
  <section class="service service--walking">
    <h2 class="service-title">DOG WALKING</h2>
    <p class="service-text">If you can't walk your dog for any reason we are here to help. 1/2 hour or hourly walks available.</p>
  </section>

  <div class="footer-rule"></div>
  <footer class="footer">
    <span class="footer-item">
      <svg width="30" height="24" viewBox="0 0 30 24"><path fill="#fff" d="M2 8c0-3 6-6 13-6s13 3 13 6v3h-6V8c-2-1-4-1.5-7-1.5S10 7 8 8v3H2z"/><path fill="#fff" d="M7 12h16l3 10H4z"/><circle cx="15" cy="17" r="3" fill="#1d5a9a"/></svg>
      0400 555 019
    </span>
    <span class="footer-item footer-item--web">
      <svg width="26" height="26" viewBox="0 0 24 24" fill="none" stroke="#fff" stroke-width="1.6"><circle cx="12" cy="12" r="10"/><ellipse cx="12" cy="12" rx="4.5" ry="10"/><path d="M2 12h20M4 6.5h16M4 17.5h16"/></svg>
      WWW.PAWHAVENEXAMPLE.COM.AU
    </span>
  </footer>
</main>
</body>
</html>
```